Stationery Design Project

We are interested in A4 paper letterheads, envelopes, maybe A4 folders where we can put the patients' results in and businesscards. No information will be given out for the time being.
We would like to see mainly shades of white.. please refer to
http://en.brivola.org/wiki/Category:Tints_of_pale
anti-flash white, splashed white,ghost white, ivory, snow and white smoke or even light grey
we are interested mainly on the silver design but we welcome the other colors as well. Since its about a gynecologist please avoid dark colors, instead use shades of beige, light grey and white

```html
<!DOCTYPE html>
<html lang="en">
<head>
<meta charset="utf-8">
<title>Stationery Design Project</title>
<link rel="stylesheet" href="https://fonts.googleapis.com/css2?family=Cinzel:wght@400;600&family=Open+Sans:wght@400&display=swap">
<style>
:root{
  --board-light:#f7f6f3;
  --board-mid:#e4e2dd;
  --ink:#3a3a3a;
  --ink-soft:#6b6b6b;
  --paper:#ffffff;
  --silver-edge:#c9c9c9;
  --silver-glow:#f5f5f5;
  --beige:#ece4d6;
  --mark:#c4c4c4;
  --mark-line:#9a9a9a;
  --footer:#d8d6d1;
  --footer-text:#3a3a3a;
}
*{margin:0;padding:0;box-sizing:border-box}
html,body{width:1200px;height:848px;overflow:hidden}
body{
  position:relative;
  background:radial-gradient(ellipse at 50% 40%,var(--board-light) 0%,var(--board-mid) 100%);
  font-family:"Cinzel",serif;color:var(--ink);
}
.corner-band{position:absolute;left:0;top:0}
.sheet{position:absolute;background:var(--paper);box-shadow:2px 3px 6px rgba(0,0,0,.22)}
.mark{display:inline-block;background:var(--mark);flex:none}
.brand{display:flex;align-items:flex-start;gap:6px}
.brand-text{line-height:1}
.brand-name{font-size:15px;letter-spacing:.3px;white-space:nowrap}
.brand-slogan{font-size:6px;text-align:right;margin-top:3px;letter-spacing:.3px;color:var(--ink-soft)}
.contact{font-size:6.5px;text-align:right;line-height:1.1;letter-spacing:.2px;color:var(--ink-soft)}

.card-front{left:113px;top:62px;width:215px;height:130px;
  background:radial-gradient(ellipse at 50% 50%,var(--silver-glow) 0%,var(--silver-edge) 85%);
  display:flex;flex-direction:column;align-items:center;justify-content:center;gap:8px}
.card-front .mark{width:26px;height:26px;background:none;border:1px solid var(--mark-line)}
.card-front .brand-name{color:var(--ink);font-size:12px}

.card-back{left:360px;top:64px;width:215px;height:128px;text-align:center}
.card-back .brand{position:absolute;left:57px;top:11px;gap:4px}
.card-back .mark{width:24px;height:24px}
.card-back .brand-name{font-size:9px}
.card-back .brand-slogan{font-size:4px}
.card-person{position:absolute;left:0;right:0;top:52px;font-size:8px;letter-spacing:.8px}
.card-title{position:absolute;left:0;right:0;top:65px;font-size:4px;letter-spacing:2px;color:var(--ink-soft)}
.card-contact{position:absolute;left:0;right:0;top:88px;font-size:4px;line-height:1.4;color:var(--ink-soft)}

.envelope-front{left:50px;top:223px;width:525px;height:267px}
.envelope-front .brand{position:absolute;left:36px;top:45px}
.envelope-front .mark{width:37px;height:37px}
.envelope-front .contact{margin-top:6px}

.envelope-back{left:50px;top:499px;width:525px;height:268px;overflow:hidden}
.envelope-flap{position:absolute;left:0;top:0}
.envelope-back .mark{position:absolute;left:243px;top:19px;width:39px;height:36px;background:none;border:1px solid var(--mark-line)}

.letterhead{left:602px;top:64px;width:545px;height:703px}
.letterhead .brand{position:absolute;left:36px;top:34px}
.letterhead .mark{width:42px;height:42px}
.letterhead .contact{margin-top:7px}
.letterhead-band{position:absolute;left:0;bottom:0;width:100%;height:61px;
  background:radial-gradient(ellipse 40% 120% at 75% 50%,var(--silver-glow) 0%,var(--silver-edge) 85%)}
.letterhead-band .mark{position:absolute;right:22px;top:14px;width:34px;height:34px;background:none;border:1px solid var(--mark-line)}

.footer{position:absolute;left:0;bottom:0;width:1200px;height:55px;background:var(--footer)}
.footer-title{position:absolute;left:62px;top:16px;font-family:"Open Sans",sans-serif;font-size:15px;color:var(--footer-text)}
</style>
</head>
<body>
<svg class="corner-band" width="230" height="110" viewBox="0 0 230 110" aria-hidden="true">
  <polygon points="0,70 190,0 230,0 0,103" fill="var(--silver-edge)"/>
</svg>

<section class="sheet card-front">
  <span class="mark"></span>
  <span class="brand-name">Company name</span>
</section>

<section class="sheet card-back">
  <div class="brand">
    <span class="mark"></span>
    <div class="brand-text">
      <div class="brand-name">Company name</div>
      <div class="brand-slogan">Company slogan</div>
    </div>
  </div>
  <div class="card-person">John Doe</div>
  <div class="card-title">Your job title here</div>
  <div class="card-contact">Company address<br>Phone : 01234 567 89 | fax : 01234 567 89<br>johndoe@companyname.com | www.yourcompanyname.com</div>
</section>

<section class="sheet envelope-front">
  <div class="brand">
    <span class="mark"></span>
    <div class="brand-text">
      <div class="brand-name">Company name</div>
      <div class="brand-slogan">Company slogan</div>
      <div class="contact">Company address<br>Phone : 01234 567 89<br>fax: 01234 567 89<br>www.yourcompanynmae.com</div>
    </div>
  </div>
</section>

<section class="sheet envelope-back">
  <svg class="envelope-flap" width="525" height="90" viewBox="0 0 525 90" aria-hidden="true">
    <defs>
      <radialGradient id="flapGlow" cx="50%" cy="30%" r="50%">
        <stop offset="0" stop-color="var(--silver-glow)"/>
        <stop offset="1" stop-color="var(--silver-edge)"/>
      </radialGradient>
    </defs>
    <polygon points="0,0 525,0 525,52 262,85 0,52" fill="url(#flapGlow)"/>
  </svg>
  <span class="mark"></span>
</section>

<section class="sheet letterhead">
  <div class="brand">
    <span class="mark"></span>
    <div class="brand-text">
      <div class="brand-name">Company name</div>
      <div class="brand-slogan">Company slogan</div>
      <div class="contact">Company address<br>Phone : 01234 567 89<br>fax: 01234 567 89<br>www.yourcompanynmae.com</div>
    </div>
  </div>
  <div class="letterhead-band"><span class="mark"></span></div>
</section>

<footer class="footer"><span class="footer-title">Stationery Design Project</span></footer>
</body>
</html>
```